Skin care manufacturer looking for packaging design for new skin care brand.

We need a design and logo for a skin care brand to be sold at retail stores and online in the United States and Europe. The design will be for 1.7oz - 2oz serums that will not have a retail box. The name of the brand is Orvia Lune and should be a luxurious brand that is approachable. The brand will consist of 4 face serums - Vitamin C, Collagen, Retinol and Hyaluronic Acid that all contain Dead Sea Minerals. Images shown are for inspiration only. Color of bottles can be varied based on design and bottles can be screen printed or labeled.

```html
<!DOCTYPE html>
<html lang="en">
<head>
<meta charset="UTF-8">
<title>Orvia Lune – Hyaluronic Acid Serum Label</title>
<link href="https://fonts.googleapis.com/css2?family=Montserrat:wght@300;400;500&display=swap" rel="stylesheet">
<style>
  :root {
    --canvas-bg: #f3f3f3;
    --label-bg: #ffffff;
    --ink: #333333;
    --ink-soft: #555555;
    --rule: #6b6b6b;
    --accent: #2ea3e3;
    --accent-text: #ffffff;
  }
  * { margin: 0; padding: 0; box-sizing: border-box; }
  html, body {
    width: 900px;
    height: 1200px;
    overflow: hidden;
    background: var(--canvas-bg);
    font-family: "Montserrat", sans-serif;
    color: var(--ink);
  }
  .canvas {
    position: relative;
    width: 900px;
    height: 1200px;
  }
  .label {
    position: absolute;
    left: 230px;
    top: 480px;
    width: 440px;
    height: 540px;
    background: var(--label-bg);
    border-radius: 8px;
    box-shadow: 0 0 0 1px #e6e6e6;
  }
  .brand-name {
    position: absolute;
    left: 0;
    right: 0;
    top: 84px;
    text-align: center;
    font-weight: 300;
    font-size: 31px;
    letter-spacing: 3px;
    color: var(--ink);
  }
  .product-line {
    position: absolute;
    left: 56px;
    top: 162px;
    width: 40px;
    height: 312px;
  }
  .product-line__text {
    position: absolute;
    left: 20px;
    top: 156px;
    transform: translate(-50%, -50%) rotate(-90deg);
    white-space: nowrap;
    font-weight: 500;
    font-size: 27px;
    letter-spacing: 1px;
    color: var(--ink);
  }
  .product-line__rule {
    position: absolute;
    left: 61px;
    top: 0;
    width: 2px;
    height: 312px;
    background: var(--rule);
  }
  .details {
    position: absolute;
    left: 146px;
    top: 220px;
    width: 210px;
  }
  .details__active {
    font-weight: 400;
    font-size: 19px;
    letter-spacing: 0.5px;
    color: var(--ink);
    padding-bottom: 8px;
    border-bottom: 1.5px solid var(--rule);
    white-space: nowrap;
  }
  .details__complex {
    margin-top: 12px;
    font-weight: 400;
    font-size: 14px;
    line-height: 20px;
    color: var(--ink-soft);
  }
  .details__benefit {
    display: inline-block;
    margin-top: 24px;
    margin-left: -6px;
    width: 212px;
    padding: 4px 0;
    background: var(--accent);
    color: var(--accent-text);
    text-align: center;
    font-weight: 400;
    font-size: 16px;
    letter-spacing: 1.5px;
  }
  .details__skin-type {
    margin-top: 10px;
    font-weight: 500;
    font-size: 10.5px;
    letter-spacing: 0.8px;
    color: var(--ink-soft);
    white-space: nowrap;
  }
  .volume {
    position: absolute;
    left: 280px;
    top: 468px;
    font-weight: 400;
    font-size: 10px;
    color: var(--ink-soft);
    white-space: nowrap;
  }
</style>
</head>
<body>
  <main class="canvas">
    <section class="label">
      <div class="brand-name">ORVIA LUNE</div>

      <div class="product-line">
        <span class="product-line__text">SKIN CARE SERUM</span>
        <span class="product-line__rule"></span>
      </div>

      <div class="details">
        <p class="details__active">HYALURONIC ACID</p>
        <p class="details__complex">WITH DEAD<br>SEA MINERALS</p>
        <p class="details__benefit">MOIST BOOSTER</p>
        <p class="details__skin-type">FOR DRY &amp; COMBINATION SKIN</p>
      </div>

      <p class="volume">20 ML / 2.0 OZ</p>
    </section>
  </main>
</body>
</html>
```